Venta Laptop Cover Skin for a DJ

I’m a wedding/corporate DJ that’s looking to have a unique laptop skin design for my Quilto laptop.

I will like to have a laptop cover skin that is a creative combination of professional, uniqueness, timeliness and looks solid.

I will like someone to take my current logo to incorporate into the design and only change the bottom “Tagline” in the logo to my new tagline listed below in the same area as the current tag.
New Tag: DJ Services | Photo Booths | Event Lighting

3D Feel
½ of laptop design with info list above and ½ laptop design with TJK attached logo
Colors: Stick with colors in my logo
Professional Design
o Note: I used this laptop for meetings and for DJ Gigs
Fonts: Open
Company Colors: Maroon / white / black

I have added our logo as an attachment, as well as our current laptop design skin. We are looking for something totally different.

Additionally, I have attached a further description of what we will like included.

• Name: DuNN HoLT ( Name need to be BIG but not over bearing ) Company Name: TJK Entertainment 2nd Co Name: TJK Management Website: www.tjkentertainment-demo.net TJK Logo Attached: See attached file o Note: EPS or AI file format of the logo can be sent to winner of the design contest PX Name: MrTJK7000 Hashtag: #TJKEntertainment Folkspace Name: TJK Entertainment

```html
<!DOCTYPE html>
<html lang="en">
<head>
<meta charset="utf-8">
<title>TJK Entertainment – Laptop Skin</title>
<link rel="stylesheet" href="https://fonts.googleapis.com/css2?family=Exo+2:wght@500&family=Saira+Condensed:wght@300;400;600&display=swap">
<style>
  :root {
    --maroon: #9b1c22;
    --ink: #1d1d1d;
    --grey-text: #3a3a3a;
    --page: #ececec;
    --skin-top: #ffffff;
    --skin-edge: #f1f1f1;
  }
  * { margin: 0; padding: 0; box-sizing: border-box; }
  html, body {
    width: 1200px; height: 800px; overflow: hidden;
    background: var(--page);
    font-family: "Saira Condensed", "Arial Narrow", sans-serif;
  }
  .skin {
    position: absolute; left: 50px; top: 60px;
    width: 1100px; height: 680px;
    border-radius: 42px;
    background: radial-gradient(ellipse at 55% 45%, var(--skin-top) 0%, var(--skin-top) 45%, var(--skin-edge) 100%);
    box-shadow: 0 14px 40px rgba(0,0,0,0.12);
    overflow: hidden;
  }
  .contour-art { position: absolute; inset: 0; width: 100%; height: 100%; }

  .socials {
    position: absolute; left: 110px; top: 52px;
    color: var(--grey-text); font-weight: 300; font-size: 17px; font-style: italic;
    display: grid; grid-template-columns: auto auto; column-gap: 34px; row-gap: 4px;
  }
  .social-item { display: flex; align-items: center; gap: 8px; }
  .social-dot { width: 12px; height: 12px; border-radius: 50%; background: var(--maroon); }
  .social-hash { color: var(--maroon); font-weight: 600; font-style: normal; font-size: 20px; line-height: 1; }

  .brand-mark {
    position: absolute; left: 110px; top: 270px;
    display: flex; flex-direction: column; align-items: flex-start;
  }
  .brand-name {
    font-family: "Saira Condensed", "Arial Narrow", sans-serif;
    font-weight: 400; font-size: 66px; line-height: 1;
    color: var(--maroon);
  }
  .tagline {
    margin-top: 22px;
    font-weight: 300; font-size: 28px; color: var(--ink); letter-spacing: 0.5px;
  }

  .owner {
    position: absolute; right: 150px; top: 135px; text-align: left;
  }
  .owner-name {
    font-family: "Exo 2", sans-serif; font-weight: 500;
    font-size: 76px; color: var(--maroon); letter-spacing: 3px; line-height: 1;
  }
  .owner-companies {
    margin-top: 6px; font-weight: 400; font-size: 22px; color: var(--grey-text);
    font-style: italic;
  }
  .owner-companies .divider { margin: 0 8px; color: #888; font-style: normal; }

  .website {
    position: absolute; left: 460px; bottom: 70px;
    font-weight: 300; font-size: 24px; letter-spacing: 5px; color: var(--ink);
    display: flex; align-items: center; gap: 14px;
  }
  .website .bar { width: 1px; height: 36px; background: var(--ink); transform: skewX(-20deg); }
</style>
</head>
<body>
  <main class="skin">
    <svg class="contour-art" viewBox="0 0 1100 680" preserveAspectRatio="none" role="img" aria-label="Faint grey flowing contour-line pattern on the right half and bottom-left corner">
      <defs>
        <radialGradient id="contourFade" cx="50%" cy="50%" r="60%">
          <stop offset="0%" stop-color="#ffffff" stop-opacity="0"/>
          <stop offset="60%" stop-color="#e9e9e9" stop-opacity="0.7"/>
          <stop offset="100%" stop-color="#e2e2e2" stop-opacity="0.9"/>
        </radialGradient>
      </defs>
      <path d="M640 0 C 600 80, 620 160, 720 230 C 800 290, 760 380, 720 460 C 690 530, 760 620, 900 640 C 1000 655, 1080 560, 1100 470 L 1100 0 Z" fill="url(#contourFade)"/>
      <path d="M0 520 C 120 470, 300 500, 360 600 C 380 640, 380 680, 380 680 L 0 680 Z" fill="url(#contourFade)"/>
    </svg>

    <section class="socials" aria-label="Social channels">
      <span class="social-item"><span class="social-dot"></span>MrTJK7000</span>
      <span class="social-item"><span class="social-dot"></span>TJK Entertainment</span>
      <span class="social-item"><span class="social-hash">#</span>#TJKEntertainment</span>
    </section>

    <section class="brand-mark">
      <p class="brand-name">TJK Entertainment</p>
      <p class="tagline">DJ Services | Photo Booths | Event Lighting</p>
    </section>

    <section class="owner">
      <h1 class="owner-name">DuNN HoLT</h1>
      <p class="owner-companies">TJK Entertainment<span class="divider">/</span>TJK Management</p>
    </section>

    <p class="website"><span class="bar"></span>WWW.TJKENTERTAINMENT-DEMO.NET</p>
  </main>
</body>
</html>
```